We need a design for a clothing tag for our summer hats & sandals line. Tag should be 2.25" high by 2" wide with a little hole punch circle in the top center. The brand is "Coral Lantern" so it should have that name on the tag & then I would also like "Summer Apparel" on the tag somewhere lower on the tag perhaps in a bit smaller font. It should obviously be summer themed- with a picture of a beach or sand- something to that effect. Our previous brand was "Misty Hours"- I have attached that artwork so you can get an idea of what we are looking for.

Logo Text

Coral Lantern

```html
<!DOCTYPE html>
<html lang="en">
<head>
<meta charset="utf-8">
<title>Coral Lantern – Summer Apparel Hang Tag</title>
<link rel="stylesheet" href="https://fonts.googleapis.com/css2?family=Open+Sans:wght@400;600&display=swap">
<style>
  :root {
    --backdrop: #e4e4e4;
    --sky-deep: #2f6fd6;
    --sky-light: #8fc4ef;
    --cloud: #e8f3fb;
    --sea: #45c7c9;
    --sand-light: #e6c99a;
    --sand-deep: #c9905a;
    --brand-blue: #4f98e4;
    --ink: #111111;
  }
  * { margin: 0; padding: 0; box-sizing: border-box; }
  html, body {
    width: 1200px;
    height: 851px;
    overflow: hidden;
    background: var(--backdrop);
  }
  .stage {
    width: 1200px;
    height: 851px;
    display: flex;
    align-items: center;
    justify-content: center;
  }
  .hang-tag {
    position: relative;
    width: 560px;
    height: 630px;
    overflow: hidden;
    box-shadow: 0 10px 30px rgba(0,0,0,0.18);
  }
  .beach-scene {
    position: absolute;
    inset: 0;
    background:
      radial-gradient(ellipse 55% 22% at 70% 42%, var(--cloud) 0%, rgba(232,243,251,0) 100%),
      linear-gradient(180deg,
        var(--sky-deep) 0%,
        var(--sky-light) 38%,
        var(--cloud) 50%,
        var(--sea) 58%,
        var(--sea) 64%,
        var(--sand-light) 70%,
        var(--sand-deep) 100%);
  }
  .punch-hole {
    position: absolute;
    top: 34px;
    left: 50%;
    width: 44px;
    height: 44px;
    margin-left: -22px;
    border-radius: 50%;
    background: var(--backdrop);
  }
  .brand-name {
    position: absolute;
    top: 180px;
    left: 0;
    right: 0;
    font-family: "Open Sans", sans-serif;
    font-size: 84px;
    font-weight: 600;
    line-height: 1.05;
    color: var(--brand-blue);
    white-space: nowrap;
  }
  .brand-name span { display: block; }
  .brand-name .first { padding-left: 56px; }
  .brand-name .second { padding-left: 150px; }
  .tagline {
    position: absolute;
    right: 40px;
    bottom: 34px;
    font-family: "Open Sans", sans-serif;
    font-size: 50px;
    font-weight: 400;
    color: var(--ink);
    white-space: nowrap;
  }
</style>
</head>
<body>
  <main class="stage">
    <article class="hang-tag">
      <div class="beach-scene" role="img" aria-label="Photo of a sunny beach: blue sky with white clouds, turquoise sea with a small palm island, and rippled golden sand"></div>
      <div class="punch-hole"></div>
      <h1 class="brand-name"><span class="first">Coral</span><span class="second">Lantern</span></h1>
      <p class="tagline">Summer Apparel</p>
    </article>
  </main>
</body>
</html>
```